I need to redesign this website. Modern Fun Professional Redesign For www.JollyPerkHub.com = New Name www.ClaimVouchly.com

Use existing content as it is on website exactly and we will revise after initial mock ups.

The new name will be ClaimVouchly.com please make a quick logo for this site too while redesigning.

Make it look like an official website....

Target Market(s)

Consumers that are redeeming certificates that businesses gave to them as a gift for customer loyalty,e tc.

Industry/Entity Type

It Professional

Logo Text

www.ClaimVouchly.com

Number of Pages Required

4 page

Colors

Designer to choose colors to be used in the design.

Requirements
Must have
• Must look professional, build trust and credibility.
Nice to have
• open
Should not have
• open

```html
<!DOCTYPE html>
<html lang="en">
<head>
<meta charset="utf-8">
<title>ClaimVouchly – Homepage</title>
<link href="https://fonts.googleapis.com/css2?family=Montserrat:wght@400;500;600;700;800&display=swap" rel="stylesheet">
<style>
:root{
  --ink:#2d2b6b;
  --purple:#5b3a9c;
  --hero:#5a55a8;
  --yellow:#f9cf33;
  --yellow-dark:#d9ac2a;
  --green:#7ccf3f;
  --green-soft:#8fd04c;
  --dark:#262626;
  --sky:#3aa8d8;
  --orange:#f08a1c;
  --white:#ffffff;
  --black:#000000;
}
*{margin:0;padding:0;box-sizing:border-box}
html,body{width:1200px;height:1200px;overflow:hidden;background:var(--black);font-family:'Montserrat',sans-serif}
.page{position:absolute;left:251px;top:83px;width:699px;height:1033px;background:var(--white);overflow:hidden}
.abs{position:absolute}
.header{left:0;top:0;width:699px;height:42px;border-top:3px solid var(--yellow);background:var(--white)}
.brand{display:flex;align-items:center;gap:5px;font-weight:700;color:var(--ink)}
.brand .mark{background:var(--purple);display:block}
.header .brand{position:absolute;left:109px;top:11px;font-size:18px}
.header .brand .mark{width:18px;height:18px}
.nav{position:absolute;right:108px;top:16px;display:flex;gap:12px;font-size:8.5px;font-weight:500;color:var(--ink)}
.nav .active{color:var(--sky)}
.hero{left:0;top:42px;width:699px;height:227px;background:linear-gradient(120deg,#6660b3,#4f4aa0 60%,#5a56a8)}
.hero h1{position:absolute;top:90px;width:100%;text-align:center;color:var(--white);font-size:12.5px;font-weight:800;letter-spacing:.3px}
.redeem{left:156px;top:196px;width:387px;height:126px;background:var(--yellow);border-radius:7px;text-align:center}
.redeem h2{margin-top:33px;font-size:8.5px;font-weight:800;color:var(--black)}
.redeem p{margin-top:4px;font-size:5.5px;color:var(--black)}
.redeem .field{position:absolute;left:41px;top:65px;width:306px;height:27px;display:flex}
.redeem .input{flex:1;background:var(--yellow-dark);color:#fbefc7;font-size:6px;padding:10px 17px;text-align:left}
.redeem .btn{width:75px;background:var(--black);color:var(--white);font-size:7.5px;font-weight:700;display:flex;align-items:center;justify-content:center;border-radius:2px}
.about{left:0;top:352px;width:699px;text-align:center}
.about h3{font-size:8px;font-weight:800;color:var(--black)}
.about p{margin-top:8px;font-size:8.5px;color:#222}
.about .quote{margin-top:5px;font-size:11px;font-weight:700;color:var(--purple)}
.help{left:0;top:427px;width:699px;height:66px;background:linear-gradient(90deg,var(--green-soft),#9bd85a 50%,#86cc44)}
.help p{position:absolute;right:283px;top:21px;text-align:right;color:var(--white);font-size:8.5px;font-weight:700;line-height:10.5px}
.help .btn{position:absolute;left:452px;top:20px;width:91px;height:26px;background:var(--white);color:var(--ink);font-size:8px;font-weight:700;display:flex;align-items:center;justify-content:center;border-radius:2px}
.reviews{left:0;top:493px;width:699px;height:281px;background:linear-gradient(180deg,var(--dark) 0%,#2a2a2a 55%,#1f1f20 100%)}
.skyline{left:0;bottom:0;width:699px;height:110px;background:linear-gradient(180deg,rgba(60,60,60,0),rgba(45,42,38,.9))}
.reviews .eyebrow{position:absolute;top:38px;width:100%;text-align:center;color:var(--white);font-size:6.5px;font-weight:600}
.reviews h2{position:absolute;top:52px;width:100%;text-align:center;color:var(--white);font-size:15px;font-weight:800}
.card{position:absolute;top:108px;width:270px;color:var(--white)}
.card .photo{position:absolute;left:0;top:0;width:78px;height:69px;border:2px solid var(--white);border-radius:3px;background:linear-gradient(135deg,#c9cbcf,#6c7480 60%,#2f3440)}
.card .name{position:absolute;left:90px;top:-1px;font-size:13px;font-weight:600}
.card .city{position:absolute;left:90px;top:21px;font-size:8.5px;font-weight:600}
.card .text{position:absolute;left:90px;top:37px;width:160px;font-size:5.6px;line-height:7.3px}
.card .date{font-size:6px;margin-top:4px}
.card .more{position:absolute;left:90px;top:105px;font-size:6px;color:var(--yellow)}
.newsletter{left:0;top:774px;width:699px;height:77px;background:var(--green)}
.newsletter .box{position:absolute;left:149px;top:22px;width:230px;height:27px;background:var(--white);box-shadow:0 2px 0 rgba(0,0,0,.08);display:flex;align-items:center;padding:0 14px;font-size:6.5px}
.newsletter .box svg{margin-right:6px}
.newsletter .ph{color:#aaa;flex:1}
.newsletter .sub{color:var(--orange);font-weight:600}
.newsletter .copy{position:absolute;left:392px;top:30px;color:var(--white)}
.newsletter .copy b{display:block;font-size:8px;font-weight:600}
.newsletter .copy span{font-size:5.8px}
.footer{left:0;top:851px;width:699px;height:127px;background:var(--white)}
.footer .brand{position:absolute;left:88px;top:32px;font-size:16px}
.footer .brand .mark{width:16px;height:16px}
.footer .about-text{position:absolute;left:88px;top:70px;width:140px;font-size:5.4px;line-height:8.5px;color:var(--ink)}
.col{position:absolute;top:31px;font-size:5.6px;line-height:8.5px;color:var(--ink)}
.col h4{font-size:6.4px;font-weight:700;color:var(--sky);margin-bottom:5px}
.col p+p{margin-top:6px}
.social{position:absolute;left:424px;top:68px;display:flex;gap:10px}
.social span{width:13px;height:13px;border-radius:50%;border:1px solid #666;display:block}
.social span.first{border-color:var(--sky)}
.bottom{left:0;top:978px;width:699px;height:55px;background:var(--purple);color:var(--white)}
.bottom .id{position:absolute;left:88px;top:23px;font-size:6.4px}
.bottom .note{position:absolute;left:282px;top:21px;width:400px;font-size:4.6px;line-height:6px;color:#b6c8ff}
</style>
</head>
<body>
<main class="page">
  <header class="abs header">
    <div class="brand"><span class="mark"></span>ClaimVouchly</div>
    <nav class="nav"><span class="active">Homepage</span><span>Contact Us</span><span>Testimonials</span><span>Terms</span></nav>
  </header>

  <section class="abs hero" role="img" aria-label="Photo of hands signing papers at a desk with laptops, tinted purple">
    <h1>WELCOME TO THE CLAIMVOUCHLY</h1>
  </section>

  <section class="abs redeem">
    <h2>PLEASE ENTER A VALID CERTIFICATE ID IN THE FORM BELOW</h2>
    <p>TO REDEEM YOUR CERTIFICATE AND TO VIEW FAQ'S, TERMS AND LOCATIONS.</p>
    <div class="field"><div class="input">Enter your text here</div><div class="btn">Get Started</div></div>
  </section>

  <section class="abs about">
    <h3>JOLLYPERKHUB.COM IS A LEADING COMPANY IN TRAVEL CERTIFICATE FULFILLMENT.</h3>
    <p>Our goal is to make it easy for you to redeem your certificate and our philosophy is this:</p>
    <div class="quote">"What good is &nbsp;it to receive a gift certificate if you can't use it?".</div>
  </section>

  <section class="abs help" role="img" aria-label="Green tinted photo of a laptop on a desk">
    <p>If you have any questions about how to redeem a certain certificate,<br>please contact us. We are here to help.</p>
    <div class="btn">Contact Now</div>
  </section>

  <section class="abs reviews">
    <div class="abs skyline" role="img" aria-label="Night city skyline photo"></div>
    <div class="eyebrow">What People say about us</div>
    <h2>TESTIMONILAS</h2>
    <article class="card" style="left:88px">
      <div class="photo" role="img" aria-label="Photo of a businessman on a phone call"></div>
      <div class="name">Nora T.</div>
      <div class="city">Athens, GA</div>
      <div class="text">"Ivy was a 'saving grace.' She followed up and helped me book the vacation and air fare. Ivy was positive and did everything she promised to do. "<div class="date">Added on 06/23/2017 06:24:16 pm</div></div>
      <div class="more">Read All Testimonilas</div>
    </article>
    <article class="card" style="left:356px">
      <div class="photo" role="img" aria-label="Photo of business people shaking hands"></div>
      <div class="name">Dana Lee M.</div>
      <div class="city">Mesa, AZ</div>
      <div class="text">"Peter was able to put together our flight schedule. He was very patient with us and diligent in working out all the changes I was requesting. Thank you, Pete. "<div class="date">Added on 05/31/2017 04:27:10 pm</div></div>
      <div class="more">Read All Testimonilas</div>
    </article>
  </section>

  <section class="abs newsletter">
    <div class="box">
      <svg width="13" height="10" viewBox="0 0 13 10"><rect x=".5" y=".5" width="12" height="9" fill="none" stroke="#f08a1c"/><path d="M.5 .5l6 5 6-5" fill="none" stroke="#f08a1c"/></svg>
      <span class="ph">Your Email Address</span><span class="sub">Subscribe Now</span>
    </div>
    <div class="copy"><b>Subscribe to our Newsletter</b><span>We will only send you important updates and notices.</span></div>
  </section>

  <footer class="abs footer">
    <div class="brand"><span class="mark"></span>ClaimVouchly</div>
    <p class="about-text">Our goal is to make it easy for you to redeem your certificate and our philosophy is this: "What good is it to receive a gift certificate if you can't use it?".</p>
    <div class="col" style="left:267px;width:130px">
      <h4>THE REDEMPTION CENTER</h4>
      <p>4120 Harbor Ridge Rd Ste B #210<br>Fairvale, Ca 90000</p>
      <p>Call 00000000 to Speak to a Mesa<br>Business Lawyer</p>
    </div>
    <div class="col" style="left:424px"><h4>EMAIL</h4><p>info@samplesite.com</p></div>
    <div class="col" style="left:524px"><h4>PHONE NO</h4><p>(000) 000-0000</p></div>
    <div class="social"><span class="first"></span><span></span><span></span><span></span><span></span></div>
  </footer>

  <section class="abs bottom">
    <div class="id">Travel ID # CST 4407318</div>
    <p class="note">Please add noreply@ClaimVouchly.com to your email safelist as this can help assure that you will receive our email response.<br>Please note that our emails could be sent to your junk or spam folders so please check there.</p>
  </section>
</main>
</body>
</html>
```